Project Sign for Construction Company

Site contractor needs a 4'x8' sign to place on construction sites for advertising. Our company builds the infrastructure for new housing developments. These sign will be posted on the road side to be viewed by passing cars. I want a clean and bold look and feel that resembles my company logo.

Font styles to use
Other font styles liked:
• Hypatia Sans Pro

Colors

Designer to choose colors to be used in the design.

Requirements
Must have
• 555-382-9146 | Info@MarlowPaving.example
• CUC 8047319
• www.MarlowPaving.example
• Services
• Road Construction
• Site Preparation & Excavation
• Underground Utilities
• Shoreline Restoration
Nice to have
• Now Hiring
• Pipe Layers
• Foremen
• Equipment Operators
Should not have
• Should not have stock picture images used in the design, focus on logo and geometric shapes

```html
<!DOCTYPE html>
<html lang="en">
<head>
<meta charset="utf-8">
<title>Marlow Paving – Site Sign</title>
<link href="https://fonts.googleapis.com/css2?family=Cabin:wght@400;500;600;700&display=swap" rel="stylesheet">
<style>
  :root {
    --brand-blue: #0b55a3;
    --charcoal: #4a4a4d;
    --light-grey: #e4e4e4;
    --page-grey: #c9c9c9;
    --white: #ffffff;
    --silver-top: #f4f4f4;
    --silver-bottom: #b9b9b9;
  }
  * { margin: 0; padding: 0; box-sizing: border-box; }
  html, body { width: 1200px; height: 1200px; overflow: hidden; }
  body {
    background: var(--page-grey);
    font-family: "Cabin", "Helvetica Neue", Arial, sans-serif;
    position: relative;
  }
  .sign {
    position: absolute;
    left: 40px; top: 320px;
    width: 1120px; height: 560px;
    background: var(--white);
    overflow: hidden;
  }
  .sign-shapes { position: absolute; inset: 0; }
  .brand {
    position: absolute;
    left: 30px; top: 170px; width: 400px;
    display: flex; flex-direction: column; align-items: center; gap: 18px;
  }
  .brand-mark {
    width: 120px; height: 120px; border-radius: 50%;
    background: var(--brand-blue);
  }
  .brand-name {
    color: var(--brand-blue);
    font-weight: 700;
    font-size: 54px;
    letter-spacing: 3px;
    text-align: center;
    line-height: 1;
  }
  .license {
    position: absolute; left: 48px; top: 512px;
    font-size: 22px; color: var(--charcoal);
  }
  .services {
    position: absolute; left: 548px; top: 56px;
    list-style: none; color: var(--white);
    font-size: 33px; font-weight: 500; line-height: 46px;
  }
  .services li::before {
    content: ""; display: inline-block;
    width: 10px; height: 10px; background: var(--white);
    margin-right: 12px; vertical-align: 6px;
  }
  .hiring-pill {
    position: absolute; left: 623px; top: 266px;
    width: 324px; height: 48px; border-radius: 24px;
    background: linear-gradient(180deg, var(--silver-top), var(--silver-bottom));
    color: var(--brand-blue);
    font-size: 42px; font-weight: 600;
    display: flex; align-items: center; justify-content: center;
    line-height: 1;
  }
  .roles {
    position: absolute; left: 490px; top: 328px;
    color: var(--white); font-size: 26px; font-weight: 500;
    white-space: nowrap; word-spacing: 2px;
  }
  .roles .sep { margin: 0 8px; }
  .phone {
    position: absolute; left: 458px; top: 395px;
    display: flex; align-items: center; gap: 10px;
    color: var(--white); font-size: 74px; font-weight: 600; line-height: 1;
  }
  .phone svg { width: 62px; height: 62px; }
  .contact {
    position: absolute; left: 420px; top: 480px;
    display: flex; gap: 20px; color: var(--white);
    font-size: 20px; line-height: 24px; white-space: nowrap;
  }
  .contact span { display: flex; align-items: center; gap: 7px; }
  .contact svg { width: 19px; height: 19px; flex: none; }
</style>
</head>
<body>
  <main class="sign">
    <svg class="sign-shapes" viewBox="0 0 1120 560" aria-hidden="true">
      <path d="M486,0 L1120,0 L1120,560 L238,560 C380,420 486,220 486,0 Z" fill="var(--light-grey)"/>
      <path d="M506,0 L1120,0 L1120,325 C1060,430 1000,500 940,560 L340,560 C460,430 506,230 506,0 Z" fill="var(--brand-blue)"/>
      <path d="M452,387 L1062,387 L982,523 L398,523 Z" fill="var(--charcoal)"/>
    </svg>

    <div class="brand">
      <div class="brand-mark"></div>
      <div class="brand-name">MARLOW<br>PAVING</div>
    </div>

    <p class="license">CUC 8047319</p>

    <ul class="services">
      <li>ROAD CONSTRUCTION</li>
      <li>SITE PREPARATION &amp; EXCAVATION</li>
      <li>UNDERGROUND UTILITIES</li>
      <li>SHORELINE RESTORATION</li>
    </ul>

    <div class="hiring-pill">NOW HIRING</div>
    <p class="roles">PIPE LAYERS<span class="sep">|</span>FOREMEN<span class="sep">|</span>EQUIPMENT OPERATORS</p>

    <div class="phone">
      <svg viewBox="0 0 64 64" aria-hidden="true">
        <path d="M14 6 L24 6 L28 20 L21 25 C25 34 30 39 39 43 L44 36 L58 40 L58 50 C58 55 54 58 49 58 C26 56 8 38 6 15 C6 10 9 6 14 6 Z" fill="var(--white)"/>
        <path d="M36 8 A20 20 0 0 1 56 28" stroke="var(--white)" stroke-width="4" fill="none"/>
        <path d="M36 17 A11 11 0 0 1 47 28" stroke="var(--white)" stroke-width="4" fill="none"/>
      </svg>
      <span>555-382-9146</span>
    </div>

    <div class="contact">
      <span>
        <svg viewBox="0 0 24 24" aria-hidden="true"><rect x="2" y="5" width="20" height="14" fill="none" stroke="var(--white)" stroke-width="2"/><path d="M2 5 L12 13 L22 5" fill="none" stroke="var(--white)" stroke-width="2"/></svg>
        Info@MarlowPaving.example
      </span>
      <span>
        <svg viewBox="0 0 24 24" aria-hidden="true"><circle cx="12" cy="12" r="10" fill="none" stroke="var(--white)" stroke-width="2"/><ellipse cx="12" cy="12" rx="4.5" ry="10" fill="none" stroke="var(--white)" stroke-width="1.6"/><path d="M2 12 H22 M4 7 H20 M4 17 H20" stroke="var(--white)" stroke-width="1.4"/></svg>
        www.MarlowPaving.example
      </span>
    </div>
  </main>
</body>
</html>
```